BRIM needs a contemporary simple brochure

We help companies understand their customers, and we would like to send a minimalistic card/brochure to potential clients to introduce our company. The card will be A6 in size (ie A5 folded once) and so will have a front, an inside front, and inside back, and a back page. It can either be portrait or landscape.
It should convey contemporary/modern, bold, fun, uncomplicated/simplicity, be clean/uncluttered, and use friendly and easy to read fonts.
Attached is the information the brochure/card should contain, together with colour palatte and another document which shows our logo, existing stationary etc to give you a feel of the brand. The background of the card could be black, yellow or white (or a combination). thanks, dave
Updates
Hi everyone. Just to let you know that the card will be A6 size, will have a matt laminate finish and can include spot uv. thanks, dave
Reason: Hi, I am looking for some better quality designs so i have extended the deadline and significantly increased the budget. thanks, dave
Target Market(s)
Marketing professionals in large corporates
Industry/Entity Type
It Company
Requirements
Must have
- use our company colours (attached)

```html
<!DOCTYPE html>
<html lang="en">
<head>
<meta charset="utf-8">
<title>BRIM – Customer &amp; Shopper Market Research</title>
<link rel="stylesheet" href="https://fonts.googleapis.com/css2?family=Open+Sans:wght@400;600&display=swap">
<style>
  :root {
    --brand-yellow: #ffcc00;
    --brand-charcoal: #414042;
    --paper: #ffffff;
    --backdrop: #c9a47c;
  }
  html, body {
    margin: 0;
    padding: 0;
    width: 1200px;
    height: 960px;
    overflow: hidden;
    background: var(--backdrop);
  }
  .brochure-spread {
    position: absolute;
    left: 50px;
    top: 92px;
    width: 1100px;
    height: 775px;
    box-shadow: 0 4px 10px rgba(0,0,0,0.35);
    font-family: "Open Sans", sans-serif;
  }
  .brochure-spread svg { display: block; }
  .wordmark { font-family: "Open Sans", sans-serif; font-weight: 600; fill: var(--paper); }
  .tagline { font-family: "Open Sans", sans-serif; font-size: 7.2px; letter-spacing: 0.5px; fill: var(--paper); }
  .contact-line { font-family: "Open Sans", sans-serif; font-size: 4.6px; fill: var(--paper); }
  .web-address { font-family: "Open Sans", sans-serif; font-size: 6.4px; letter-spacing: 3px; fill: var(--brand-charcoal); }
</style>
</head>
<body>
<div class="brochure-spread">
  <svg width="1100" height="775" viewBox="0 0 596 420" xmlns="http://www.w3.org/2000/svg">
    <defs>
      <linearGradient id="steelBand" x1="0" y1="0" x2="0" y2="1">
        <stop offset="0" stop-color="#d6d6d6"/>
        <stop offset="0.55" stop-color="#a4a4a4"/>
        <stop offset="1" stop-color="#6c6c6c"/>
      </linearGradient>
      <linearGradient id="interiorTones" x1="0" y1="0" x2="0" y2="1">
        <stop offset="0" stop-color="#3d4a3a"/>
        <stop offset="0.3" stop-color="#7d8c6a"/>
        <stop offset="0.55" stop-color="#e6e3dc"/>
        <stop offset="0.8" stop-color="#8a6f5c"/>
        <stop offset="1" stop-color="#414042"/>
      </linearGradient>
      <linearGradient id="mapTones" x1="0" y1="0" x2="1" y2="0">
        <stop offset="0" stop-color="#6e6e6e" stop-opacity="0.6"/>
        <stop offset="0.5" stop-color="#5a5a5a" stop-opacity="0.7"/>
        <stop offset="1" stop-color="#7a7a7a" stop-opacity="0.5"/>
      </linearGradient>
    </defs>

    <!-- base panels -->
    <rect class="panel-base" x="0" y="0" width="596" height="420" fill="var(--brand-charcoal)"/>
    <rect class="top-band" x="0" y="0" width="596" height="32" fill="var(--brand-yellow)"/>
    <rect class="bottom-band" x="0" y="396" width="596" height="24" fill="var(--brand-yellow)"/>
    <rect class="steel-band" x="0" y="148" width="596" height="105" fill="url(#steelBand)"/>
    <polygon class="drop-pointer" points="257,31 337,31 296,148" fill="var(--brand-yellow)"/>

    <!-- back cover -->
    <rect class="world-map" x="55" y="158" width="187" height="88" rx="6" fill="url(#mapTones)"
          role="img" aria-label="Dotted world map"/>

    <g class="back-contact">
      <text class="wordmark" x="148" y="345" font-size="20" text-anchor="middle">brim</text>
      <text class="contact-line" x="148" y="356" text-anchor="middle">Level 4</text>
      <text class="contact-line" x="148" y="362" text-anchor="middle">21 Harbour Lane</text>
      <text class="contact-line" x="148" y="368" text-anchor="middle">Eastfield, NSW, 2150</text>
      <text class="contact-line" x="148" y="381" text-anchor="middle">02 5550 1942</text>
      <text class="contact-line" x="148" y="387" text-anchor="middle">info@brimmr.com.au</text>
    </g>

    <!-- front cover -->
    <text class="wordmark front-brand" x="445" y="101" font-size="42" text-anchor="middle">brim</text>
    <rect class="lounge-photo" x="337" y="118" width="218" height="158" fill="url(#interiorTones)"
          role="img" aria-label="Photo of a bright modern lounge with white sofas and indoor plants"/>
    <text class="tagline" x="446" y="296" text-anchor="middle">Customer &amp; Shopper Market Research</text>

    <text class="web-address" x="445" y="410" text-anchor="middle">www.brimmr.com.au</text>
  </svg>
</div>
</body>
</html>
```